Interior Design/ New Construction interior finishes

Interior Design Website

Target Market(s)

Home builders, New Construction, Renovations, Public

Industry/Entity Type

Construction

Coding

Coded - Design and coding required

Number of Pages Required

1 page

Font styles to use
Sans Serif

Colors

Designer to choose colors to be used in the design.

Requirements
Must have
• Section to upload pictures of projects
• Simple and modern design
• Designer 1 details about myself
• Logo
• Upload section for photos for future jobs
Nice to have
• Sections they can click on to see certain rooms in a house
• Decorating, floral arrangements, holiday decorating.
• I have lots of before and after as well. Maybe a section for those.

```html
<!DOCTYPE html>
<html lang="en">
<head>
<meta charset="utf-8">
<title>Vela Designs — Interior Design</title>
<link rel="stylesheet" href="https://fonts.googleapis.com/css2?family=Raleway:wght@300;400;500;600;700&display=swap">
<style>
:root{
  --ink:#0c0c0c;
  --ink-soft:#1c1c1c;
  --white:#ffffff;
  --paper:#e9e9e9;
  --card:#d4d4d4;
  --tab:#e4e4e4;
  --text:#222222;
  --muted:#8a8a8a;
  --footer-text:#cfcfcf;
}
*{margin:0;padding:0;box-sizing:border-box}
html,body{width:1200px;height:2752px;overflow:hidden}
body{font-family:'Raleway',Arial,sans-serif;color:var(--text);background:var(--white);position:relative}
.abs{position:absolute}

/* navigation */
.nav{position:absolute;top:0;left:0;width:1200px;height:50px;background:var(--ink)}
.nav a{position:absolute;top:0;height:50px;line-height:50px;color:var(--white);font-size:15px;text-decoration:none;text-align:center}
.nav a.active{background:var(--tab);color:var(--ink);left:88px;width:98px}
.nav .search{position:absolute;left:1066px;top:16px}

/* hero */
.hero{position:absolute;top:50px;left:0;width:1200px;height:537px;
  background:linear-gradient(100deg,#6a5340 0%,#8c7a66 22%,#b9b2a8 45%,#d9d7d3 65%,#c8c1b6 82%,#8b6d4f 100%)}
.hero-logo{position:absolute;left:0;width:1200px;top:148px;text-align:center;color:var(--white)}
.hero-logo .mark{width:110px;height:110px;border:4px solid var(--white);border-radius:50%;margin:0 auto 14px}
.hero-logo .name{font-size:40px;font-weight:400;letter-spacing:4px}
.hero .arrows{position:absolute;left:560px;top:440px}

/* welcome */
.welcome{position:absolute;top:587px;left:0;width:1200px;height:318px;background:var(--ink);color:var(--white);text-align:center}
.section-title{font-weight:400;font-size:38px;letter-spacing:1px}
.rule{width:46px;height:3px;margin:16px auto 0}
.welcome .section-title{padding-top:63px}
.welcome .rule{background:var(--white)}
.welcome p{width:1040px;margin:22px auto 0;font-size:14px;line-height:25px}
.btn{display:inline-block;margin-top:26px;background:var(--ink-soft);color:var(--white);font-size:14px;font-weight:700;padding:12px 20px;letter-spacing:.5px}

/* features */
.features{position:absolute;top:905px;left:0;width:1200px;height:743px;background:var(--paper);text-align:center}
.features .section-title{padding-top:56px;color:var(--ink)}
.features .rule,.before-after .rule,.testimonials .rule{background:var(--ink)}
.features .intro{width:1060px;margin:22px auto 0;font-size:14px;line-height:25px}
.card{position:absolute;top:212px;width:332px;height:421px}
.card .photo{width:100%;height:210px}
.card .body{width:100%;height:211px;background:var(--card);padding:0 34px}
.card h3{font-weight:500;font-size:23px;letter-spacing:1px;margin-top:34px}
.card p{font-size:15px;line-height:24px;margin-top:16px;text-align:justify;text-align-last:center}
.dots{position:absolute;top:686px;left:575px}

/* before & after */
.before-after{position:absolute;top:1648px;left:0;width:1200px;height:399px;background:var(--white);text-align:center}
.before-after .section-title{padding-top:35px;color:var(--ink)}
.ba-row{position:absolute;top:115px;left:74px;width:1054px;height:232px}
.ba-pane{position:absolute;top:0;height:232px}
.ba-label{position:absolute;color:var(--white);font-size:22px;font-weight:400;letter-spacing:1px}
.play{position:absolute;width:38px;height:38px;border-radius:50%;background:var(--white)}

/* testimonials */
.testimonials{position:absolute;top:2047px;left:0;width:1200px;height:393px;background:var(--paper);text-align:center}
.testimonials .section-title{padding-top:72px;color:var(--ink)}
.testimonials blockquote{width:940px;margin:42px auto 0;font-size:22px;line-height:33px;color:var(--ink)}
.testimonials .author{margin-top:22px;font-size:13px;font-weight:500}
.testimonials .pager{position:absolute;top:318px;left:565px}

/* footer */
.footer{position:absolute;top:2440px;left:0;width:1200px;height:312px;background:var(--ink);color:var(--white)}
.footer .brand-mark{position:absolute;left:110px;top:18px;width:54px;height:54px;border:3px solid var(--white);border-radius:50%}
.footer .brand-name{position:absolute;left:76px;top:76px;font-size:20px;letter-spacing:2px}
.footer .about{position:absolute;left:76px;top:106px;width:258px;font-size:13px;line-height:22px;color:var(--footer-text)}
.footer .read-more{position:absolute;left:76px;top:206px;font-size:12px;color:#5a5a5a}
.footer h4{position:absolute;top:68px;font-size:20px;font-weight:500}
.links a{position:absolute;font-size:13px;color:var(--footer-text);text-decoration:none}
.links a::before{content:"›";margin-right:14px;color:var(--muted)}
.contact-item{position:absolute;left:638px;font-size:13px;line-height:20px;color:var(--footer-text)}
.contact-item svg{position:absolute;left:0;top:0}
.contact-item span{position:absolute;left:52px;white-space:nowrap}
.social{position:absolute;left:946px;top:108px}
.copy{position:absolute;left:946px;font-size:12px;color:var(--footer-text)}
</style>
</head>
<body>

<nav class="nav">
  <a class="active" href="#">Home</a>
  <a href="#" style="left:208px;width:66px">About Us</a>
  <a href="#" style="left:322px;width:66px">Features</a>
  <a href="#" style="left:434px;width:104px">Before &amp; After</a>
  <a href="#" style="left:584px;width:82px">Contact Us</a>
  <svg class="search" width="20" height="20" viewBox="0 0 20 20"><circle cx="8" cy="8" r="5.5" fill="none" stroke="#fff" stroke-width="2.4"/><line x1="12" y1="12" x2="17" y2="17" stroke="#fff" stroke-width="2.8" stroke-linecap="round"/></svg>
</nav>

<header class="hero" role="img" aria-label="Photo of a bright open-plan dining room and white kitchen with wooden floors">
  <div class="hero-logo">
    <div class="mark"></div>
    <div class="name">Vela Designs</div>
  </div>
  <svg class="arrows" width="80" height="50" viewBox="0 0 80 50"><polyline points="22,8 6,25 22,42" fill="none" stroke="#fff" stroke-width="3"/><polyline points="58,8 74,25 58,42" fill="none" stroke="#fff" stroke-width="3"/></svg>
</header>

<section class="welcome">
  <h1 class="section-title">WELCOME TO VELA DESIGNS</h1>
  <div class="rule"></div>
  <p>Aliquam molestie, mi et imperdiet euismod, dui purus auctor tellus, et interdum lacus lectus et ante. Sed accumsan sollicitudin sapien, sit amet adipiscing turpis gravida ac. In congue, neque ac lobortis volutpat, libero mauris varius mi, vitae suscipit ipsum ligula vitae risus. Duis aliquam nibh a dui iaculis viverra id a velit. Vivamus egestas risus in magna varius commodo.</p>
  <span class="btn">READ MORE</span>
</section>

<section class="features">
  <h2 class="section-title">OUR FEATURES</h2>
  <div class="rule"></div>
  <p class="intro">Aliquam molestie, mi et imperdiet euismod, dui purus auctor tellus, et interdum lacus lectus et ante. Sed accumsan sollicitudin sapien, sit amet adipiscing turpis gravida ac. In congue, neque ac lobortis volutpat, libero mauris varius mi,</p>

  <article class="card" style="left:74px">
    <div class="photo" role="img" aria-label="Photo of a styled bedroom with orchids" style="background:linear-gradient(90deg,#c9c6c4,#8f8c8f 55%,#6d6470)"></div>
    <div class="body"><h3>DECORATING</h3><p>Arcu dolor eu ut nam pede. Ut neque sem. Ante curabitur metus diam ligula facilisis dui euismod etiam aliquet feugiat</p></div>
  </article>

  <article class="card" style="left:435px">
    <div class="body"><h3>FLORAL ARRANGEMENTS</h3><p>Arcu dolor eu ut nam pede. Ut neque sem. Ante curabitur metus diam ligula facilisis dui euismod etiam aliquet feugiat</p></div>
    <div class="photo" role="img" aria-label="Photo of a potted succulent on a white shelf" style="background:linear-gradient(180deg,#ededed,#d9dcd6 60%,#a9aa9e)"></div>
  </article>

  <article class="card" style="left:795px">
    <div class="photo" role="img" aria-label="Photo of a family decorating a holiday tree" style="background:linear-gradient(90deg,#e4e2e0,#c9bfb5 45%,#3f5a3a 80%,#2d4a2c)"></div>
    <div class="body"><h3>HOLIDAY DECORATING</h3><p>Arcu dolor eu ut nam pede. Ut neque sem. Ante curabitur metus diam ligula facilisis dui euismod etiam aliquet feugiat</p></div>
  </article>

  <svg class="dots" width="50" height="10" viewBox="0 0 50 10"><circle cx="5" cy="5" r="4.5" fill="#555"/><circle cx="25" cy="5" r="4.5" fill="#555"/><circle cx="45" cy="5" r="4.5" fill="#555"/></svg>
</section>

<section class="before-after">
  <h2 class="section-title">BEFORE &amp; AFTER</h2>
  <div class="rule"></div>
  <div class="ba-row">
    <div class="ba-pane" role="img" aria-label="Photo of a bathroom under renovation" style="left:0;width:262px;background:linear-gradient(90deg,#6f7a72,#8f9a92 50%,#6d7570)"></div>
    <div class="ba-pane" role="img" aria-label="Photo of the finished bathroom with shower" style="left:262px;width:265px;background:linear-gradient(90deg,#b88a2a,#dba12a 40%,#b0aea8 70%,#3c3430)"></div>
    <div class="ba-pane" role="img" aria-label="Photo of an empty room with glass doors before work" style="left:527px;width:263px;background:linear-gradient(90deg,#4d4d4d,#7a7a78 50%,#5e5e5c)"></div>
    <div class="ba-pane" role="img" aria-label="Photo of the finished room with glass doors and dining set" style="left:790px;width:264px;background:linear-gradient(90deg,#d6d6d4,#5b6a52 50%,#e2e0dc)"></div>
    <span class="ba-label" style="left:84px;top:106px">BEFORE</span>
    <span class="ba-label" style="left:614px;top:100px">BEFORE</span>
    <span class="play" style="left:243px;top:97px"><svg width="38" height="38" viewBox="0 0 38 38"><polygon points="15,11 27,19 15,27" fill="#111"/></svg></span>
    <span class="play" style="left:771px;top:97px"><svg width="38" height="38" viewBox="0 0 38 38"><polygon points="15,11 27,19 15,27" fill="#111"/></svg></span>
  </div>
</section>

<section class="testimonials">
  <h2 class="section-title">TESTIMONIALS</h2>
  <div class="rule"></div>
  <blockquote>“Aliquet nibh vel facilisis ipsum libero a justo arcu. Ad vitae rutrum nec proin quis. Proin feugiat quis ut quam risus”</blockquote>
  <div class="author">Mara Quill</div>
  <svg class="pager" width="72" height="12" viewBox="0 0 72 12"><circle cx="6" cy="6" r="4.5" fill="#555"/><circle cx="21" cy="6" r="4" fill="none" stroke="#555"/><circle cx="36" cy="6" r="4" fill="none" stroke="#555"/><circle cx="51" cy="6" r="4" fill="none" stroke="#555"/><circle cx="66" cy="6" r="4" fill="none" stroke="#555"/></svg>
</section>

<footer class="footer">
  <div class="brand-mark"></div>
  <div class="brand-name">Vela Designs</div>
  <p class="about">Morbi et orci. Nulla quam a. Diam sapien eu a nisi dignissim. Vestibulum et sit arcu turpis commodo. Sem nec quis. Tortor mi dictum. Neque et amet euismod...</p>
  <span class="read-more">Read more</span>

  <h4 style="left:374px">Quick Links</h4>
  <div class="links">
    <a href="#" style="left:376px;top:106px">Home</a>
    <a href="#" style="left:376px;top:139px">About</a>
    <a href="#" style="left:376px;top:172px">Features</a>
    <a href="#" style="left:488px;top:106px">Before &amp; After</a>
    <a href="#" style="left:488px;top:139px">Contact Us</a>
  </div>

  <h4 style="left:638px">Contact Us</h4>
  <div class="contact-item" style="top:108px">
    <svg width="36" height="36" viewBox="0 0 36 36"><circle cx="18" cy="18" r="17" fill="none" stroke="#555"/><path d="M18 9a6 6 0 0 0-6 6c0 5 6 12 6 12s6-7 6-12a6 6 0 0 0-6-6z" fill="#ccc"/><circle cx="18" cy="15" r="2.2" fill="#0c0c0c"/></svg>
    <span style="top:0">#123, Lorium ipsum, Dolor<br>Amit. Newzland.</span>
  </div>
  <div class="contact-item" style="top:164px">
    <svg width="36" height="36" viewBox="0 0 36 36"><circle cx="18" cy="18" r="17" fill="none" stroke="#555"/><rect x="10" y="12" width="16" height="12" rx="1" fill="#ccc"/><polyline points="10,12 18,19 26,12" fill="none" stroke="#0c0c0c" stroke-width="1.5"/></svg>
    <span style="top:8px">hello@veladesigns.com</span>
  </div>
  <div class="contact-item" style="top:220px">
    <svg width="36" height="36" viewBox="0 0 36 36"><circle cx="18" cy="18" r="17" fill="none" stroke="#555"/><path d="M13 10l3 0 1.5 4-2 1.5a9 9 0 0 0 5 5l1.5-2 4 1.5 0 3a2 2 0 0 1-2 2A14 14 0 0 1 11 12a2 2 0 0 1 2-2z" fill="#ccc"/></svg>
    <span style="top:8px">1-800 555 0142</span>
  </div>

  <h4 style="left:950px">Follow Us</h4>
  <svg class="social" width="176" height="40" viewBox="0 0 176 40"><circle cx="18" cy="20" r="17" fill="none" stroke="#777" stroke-width="1.5"/><circle cx="64" cy="20" r="17" fill="none" stroke="#777" stroke-width="1.5"/><circle cx="110" cy="20" r="17" fill="none" stroke="#777" stroke-width="1.5"/><circle cx="156" cy="20" r="17" fill="none" stroke="#777" stroke-width="1.5"/></svg>
  <span class="copy" style="top:170px">© 2018. Company Name</span>
  <span class="copy" style="top:200px">All Right Reserved</span>
</footer>

</body>
</html>
```